Brambury Logistics

Create a modern, simple, Elegant business card design for my business.

Services: Tamo Trucks, Transport, Contract Logistics,

Industry/Entity Type

Business

Contact Information for Business Card

Include all details same as old card plus new website address: www.bramburylogistics.com.au

Requirements
Must have
• Similar colors to Logo.

```html
<!DOCTYPE html>
<html lang="en">
<head>
<meta charset="utf-8">
<title>Brambury Logistics – Business Card</title>
<link rel="stylesheet" href="https://fonts.googleapis.com/css2?family=Roboto:wght@400;500;700&display=swap">
<style>
  :root {
    --bg: #e9e7e3;
    --card-white: #f4f4f4;
    --card-white-edge: #e2e2e2;
    --blue: #0b64a3;
    --blue-dark: #064f86;
    --grey-block: #8a8b8e;
    --grey-text: #8c8d90;
    --title-blue: #2a7fc0;
    --white: #ffffff;
  }
  * { box-sizing: border-box; margin: 0; padding: 0; }
  html, body { width: 1200px; height: 1023px; overflow: hidden; }
  body {
    background: var(--bg);
    font-family: "Roboto", sans-serif;
    position: relative;
  }
  .card {
    position: absolute;
    left: 320px;
    width: 560px;
    height: 320px;
    border-radius: 14px;
    overflow: hidden;
    box-shadow: 0 10px 28px rgba(0,0,0,0.18);
  }

  /* Front */
  .card-front {
    top: 110px;
    background: linear-gradient(180deg, var(--card-white), var(--card-white-edge));
  }
  .front-name {
    position: absolute;
    right: 34px;
    top: 30px;
    text-align: right;
  }
  .front-name .person { font-size: 26px; color: var(--grey-text); letter-spacing: 1px; }
  .front-name .role { font-size: 13px; color: var(--title-blue); margin-top: 1px; }
  .front-brand {
    position: absolute;
    left: 30px;
    top: 70px;
    display: flex;
    align-items: center;
    gap: 10px;
    font-size: 24px;
    font-weight: 700;
    color: var(--blue);
  }
  .front-brand .mark { width: 16px; height: 16px; background: var(--blue); }
  .grey-block {
    position: absolute;
    right: 0;
    top: 140px;
    width: 108px;
    height: 30px;
    background: var(--grey-block);
  }
  .blue-band {
    position: absolute;
    left: 0;
    right: 0;
    top: 176px;
    height: 112px;
    background: linear-gradient(90deg, var(--blue-dark), var(--blue));
  }
  .contact-list {
    position: absolute;
    left: 30px;
    top: 14px;
    list-style: none;
    color: var(--white);
    font-size: 15px;
    letter-spacing: 0.6px;
  }
  .contact-list li { display: flex; align-items: center; gap: 9px; height: 21px; }
  .contact-list svg { width: 13px; height: 13px; flex: none; }

  /* Back */
  .card-back {
    top: 570px;
    background: linear-gradient(160deg, var(--blue-dark), var(--blue) 60%, var(--blue-dark));
  }
  .back-brand {
    position: absolute;
    left: 0;
    right: 0;
    top: 96px;
    text-align: center;
    font-size: 44px;
    font-weight: 700;
    color: var(--white);
    letter-spacing: 1px;
  }
  .services {
    position: absolute;
    left: 0;
    right: 0;
    top: 232px;
    text-align: center;
    font-size: 16px;
    color: var(--white);
    letter-spacing: 0.8px;
    word-spacing: 4px;
  }
  .white-stripe {
    position: absolute;
    left: 0;
    right: 0;
    top: 266px;
    height: 30px;
    background: var(--card-white);
  }
</style>
</head>
<body>

<section class="card card-front" aria-label="Business card front">
  <div class="front-name">
    <div class="person">Your Name</div>
    <div class="role">Title</div>
  </div>
  <div class="front-brand"><span class="mark"></span>Brambury Logistics</div>
  <div class="grey-block"></div>
  <div class="blue-band">
    <ul class="contact-list">
      <li>
        <svg viewBox="0 0 16 16" aria-hidden="true"><circle cx="8" cy="8" r="7" fill="none" stroke="#fff" stroke-width="1.5"/><path d="M5.5 4.5l1.5 1.5-1 1c.6 1.3 1.6 2.3 2.9 2.9l1-1 1.5 1.5-1 1.2c-2.6-.4-5.1-2.9-5.5-5.5z" fill="#fff"/></svg>
        0400 555 318
      </li>
      <li>
        <svg viewBox="0 0 16 16" aria-hidden="true"><rect x="1.5" y="3.5" width="13" height="9" fill="none" stroke="#fff" stroke-width="1.5"/><path d="M1.5 3.5l6.5 5 6.5-5M1.5 12.5l4.5-4.5M14.5 12.5l-4.5-4.5" fill="none" stroke="#fff" stroke-width="1.2"/></svg>
        Kel@bramburylogistics.com.au
      </li>
      <li>
        <svg viewBox="0 0 16 16" aria-hidden="true"><circle cx="8" cy="8" r="6.5" fill="none" stroke="#fff" stroke-width="1.4"/><path d="M1.5 8h13M8 1.5c-3 3.5-3 9.5 0 13M8 1.5c3 3.5 3 9.5 0 13" fill="none" stroke="#fff" stroke-width="1.1"/></svg>
        www.bramburylogistics.com.au
      </li>
      <li>
        <svg viewBox="0 0 16 16" aria-hidden="true"><path d="M8 15s-5-5.3-5-8.5a5 5 0 0110 0C13 9.7 8 15 8 15z" fill="none" stroke="#fff" stroke-width="1.5"/><circle cx="8" cy="6.5" r="1.8" fill="#fff"/></svg>
        Western Australia
      </li>
    </ul>
  </div>
</section>

<section class="card card-back" aria-label="Business card back">
  <div class="back-brand">Brambury Logistics</div>
  <div class="services">Tamo Trucks | Transport | Contract Logistics</div>
  <div class="white-stripe"></div>
</section>

</body>
</html>
```